Business Card - Professional Minimalist - Double sided

We appreciate minimalist logo/web/collateral designs that allow design to tell a story. We want to relay a professional image/approach but throwing in a splash of modern when we’re able so long as it’s not distracting. Think 75% classic corporate, 25% modern. Open to black or white design, not sure which might look the best.

Target Market(s)

Senior executives or related government affairs contacts within the agriculture, energy, and defense industries (i.e., potential clients) but located outside of Washington, DC. Most potential clients based in DC with be familiar with both of us and our shared history.

Industry/Entity Type

Consulting

Contact Information for Business Card

Name: Daniel R. Whitlock
Title: Co-Founder & Partner
Address: 418 Bramblewood Ave. SE | Suite 2716 | Washington, D.C. 20019
Phone: (202) 555-0187
Email: Daniel@HollerbyWhitlock.com

Font styles to use
Serif

Colors

Designer to choose only greyscale colors for use in the design.

Requirements
Must have
• Name: Daniel R. Whitlock
Phone: (202) 555-0187

```html
<!DOCTYPE html>
<html lang="en">
<head>
<meta charset="utf-8">
<title>Hollerby Whitlock Group – Business Card</title>
<link href="https://fonts.googleapis.com/css2?family=Tinos:wght@400;700&display=swap" rel="stylesheet">
<style>
  :root {
    --canvas-bg: #3a3c40;
    --card-bg: #2a2a2c;
    --card-edge: #c9c9c9;
    --text-main: #d6d6d6;
    --text-soft: #a9a9a9;
    --logo-grey: #8e8e8e;
    --rule: #8a8a8a;
  }
  * { box-sizing: border-box; margin: 0; padding: 0; }
  html, body { width: 1200px; height: 900px; overflow: hidden; }
  body {
    background: var(--canvas-bg);
    font-family: "Tinos", "Times New Roman", serif;
    position: relative;
  }
  .card {
    position: absolute;
    left: 320px;
    width: 560px;
    height: 320px;
    background: var(--card-bg);
    border: 4px solid var(--card-edge);
    border-radius: 20px;
    overflow: hidden;
  }
  .card--front { top: 70px; }
  .card--back { top: 500px; }

  .wordmark {
    position: absolute;
    display: flex;
    align-items: center;
    gap: 12px;
    color: var(--logo-grey);
    font-weight: 400;
    font-size: 19px;
    letter-spacing: 3px;
    text-transform: uppercase;
  }
  .wordmark__square {
    width: 34px; height: 34px;
    border: 2px solid var(--logo-grey);
    flex: none;
  }
  .wordmark__name { line-height: 1.35; white-space: nowrap; }

  .card--front .wordmark { left: 28px; top: 118px; font-size: 14px; letter-spacing: 1.5px; }

  .front-divider { position: absolute; left: 0; top: 0; }

  .contact {
    position: absolute;
    left: 312px;
    top: 40px;
    color: var(--text-main);
  }
  .contact__name { font-weight: 700; font-size: 24px; margin-bottom: 4px; white-space: nowrap; }
  .contact__title { font-size: 16px; color: var(--text-soft); margin-bottom: 14px; }
  .contact__row {
    display: flex;
    align-items: flex-start;
    gap: 9px;
    font-size: 15px;
    color: var(--text-soft);
    margin-bottom: 8px;
    line-height: 1.3;
    white-space: nowrap;
  }
  .contact__icon { width: 18px; height: 18px; flex: none; margin-top: 1px; }

  .back-pattern { position: absolute; inset: 0; }
  .card--back .wordmark { left: 50%; top: 50%; transform: translate(-50%, -50%); font-size: 24px; white-space: nowrap; }
</style>
</head>
<body>

<section class="card card--front" aria-label="Business card front">
  <svg class="front-divider" width="552" height="312" viewBox="0 0 552 312" aria-hidden="true">
    <defs>
      <linearGradient id="dividerFade" x1="0" y1="0" x2="0" y2="1">
        <stop offset="0" stop-color="#9a9a9a" stop-opacity="0"/>
        <stop offset="0.5" stop-color="#b5b5b5" stop-opacity="1"/>
        <stop offset="1" stop-color="#9a9a9a" stop-opacity="0"/>
      </linearGradient>
    </defs>
    <line x1="290" y1="30" x2="240" y2="282" stroke="url(#dividerFade)" stroke-width="1.5"/>
  </svg>

  <div class="wordmark">
    <span class="wordmark__square"></span>
    <span class="wordmark__name">Hollerby Whitlock<br>Group</span>
  </div>

  <div class="contact">
    <p class="contact__name">Daniel R. Whitlock</p>
    <p class="contact__title">Co-Founder &amp; Partner</p>
    <p class="contact__row">
      <svg class="contact__icon" viewBox="0 0 20 20" aria-hidden="true">
        <rect x="1" y="1" width="18" height="18" rx="3" fill="#bdbdbd"/>
        <path d="M7 5c-1 0-2 1-2 2 0 4 4 8 8 8 1 0 2-1 2-2l-2-2-1.5 1c-1.5-.6-2.9-2-3.5-3.5L9 7z" fill="#2a2a2c"/>
      </svg>
      (202) 555-0187
    </p>
    <p class="contact__row">
      <svg class="contact__icon" viewBox="0 0 20 20" aria-hidden="true">
        <rect x="1" y="4" width="18" height="12" fill="#bdbdbd"/>
        <path d="M1 4l9 7 9-7" fill="none" stroke="#2a2a2c" stroke-width="1.5"/>
      </svg>
      Daniel@HollerbyWhitlock.com
    </p>
    <p class="contact__row">
      <svg class="contact__icon" viewBox="0 0 20 20" aria-hidden="true">
        <path d="M10 1a6 6 0 0 0-6 6c0 5 6 12 6 12s6-7 6-12a6 6 0 0 0-6-6z" fill="#bdbdbd"/>
        <circle cx="10" cy="7" r="2.3" fill="#2a2a2c"/>
      </svg>
      <span>418 Bramblewood Ave. SE |<br>Suite 2716 |<br>Washington, D.C. 20019</span>
    </p>
  </div>
</section>

<section class="card card--back" aria-label="Business card back">
  <svg class="back-pattern" width="552" height="312" viewBox="0 0 552 312" role="img" aria-label="Subtle dark diamond pattern background">
    <defs>
      <linearGradient id="backSheen" x1="0" y1="0" x2="1" y2="1">
        <stop offset="0" stop-color="#333335"/>
        <stop offset="0.5" stop-color="#29292b"/>
        <stop offset="1" stop-color="#222224"/>
      </linearGradient>
    </defs>
    <rect width="552" height="312" fill="url(#backSheen)"/>
  </svg>
  <div class="wordmark">
    <span class="wordmark__square"></span>
    <span class="wordmark__name">Hollerby Whitlock Group</span>
  </div>
</section>

</body>
</html>
```